Business Improvement Consultancy needs web design

I need a web design for my company, that offers support to manufacturing and distribution businesses.

We have worked with a range of organisations to help them get more out of their operational processes and supply chains.

With full end to end supply chain knowledge we help them identify waste in their supply chains that often get overlooked.

We support through a number of offerings

Developing an end to end supply chain strategy

Applying Lean to support the strategy

Interim support network to deliver quick wins and rapid cost improvement

Project Management

Interactive training tools for delivering supply chain best practice.

I have the logos done already, so it is more about look and feel, and the colour schemes etc giving a professional feel.

Also have the web domains www.veltrosiga.co, www.veltrosiga.co.uk & www.veltrosiga.eu, using Q&Q starter bundle

Target Market(s)

Manufacturing and distribution businesses, potentially other consultancies looking for collaboration

Industry/Entity Type

Business

Requirements
Must have
• Some pictures on related to performance improvement, bar charts showing productivity growth / increase.

Should have the chatterbox quipper and worknodes logos to share the website

```html
<!DOCTYPE html>
<html lang="en">
<head>
<meta charset="utf-8">
<title>Veltrosiga Europe</title>
<link href="https://fonts.googleapis.com/css2?family=Arimo:wght@400;700&family=Roboto+Condensed:wght@400&family=Source+Sans+3:wght@400;600&display=swap" rel="stylesheet">
<style>
:root{
  --purple:#3b3286;
  --purple-deep:#2e2670;
  --purple-mid:#4a42a0;
  --purple-light:#6a62b8;
  --nav-top:#6257b4;
  --nav-bottom:#3f3592;
  --ink:#2b2b3a;
  --body-grey:#666;
  --hero-grey:#5c5c66;
  --on-purple:#e9e8f5;
  --link:#1a6fc4;
  --footer-bg:#efeff1;
  --line:#d8d8de;
}
*{box-sizing:border-box;margin:0;padding:0}
html,body{width:1040px;height:1200px;overflow:hidden;background:#fff}
body{position:relative;font-family:"Arimo",Arial,sans-serif;color:var(--ink)}
h1,h2,h3{font-weight:400}

/* navigation */
.main-nav{position:absolute;left:0;top:0;width:1040px;height:38px;background:linear-gradient(var(--nav-top),var(--nav-bottom))}
.main-nav a{position:absolute;top:10px;font-family:"Roboto Condensed",Arial,sans-serif;font-size:15px;color:#fff;text-decoration:none;transform:translateX(-50%);white-space:nowrap}
.main-nav .current-tab{position:absolute;left:343px;top:0;width:92px;height:50px;background:linear-gradient(#fff,#e6e6ea);box-shadow:0 3px 6px rgba(0,0,0,.18);z-index:1}
.main-nav a.current{color:var(--purple-deep);z-index:2;top:12px}

/* hero */
.hero{position:absolute;left:0;top:38px;width:1040px;height:398px;background:linear-gradient(#e4e4ea 0%,#f4f4f7 60%,#fbfbfc 82%,#ececf0 100%)}
.brand{position:absolute;left:24px;top:63px;display:flex;align-items:center;gap:16px}
.brand-dot{width:46px;height:46px;border-radius:50%;background:var(--purple-deep)}
.brand-name{font-family:"Source Sans 3",sans-serif;font-size:31px;color:var(--purple-deep);font-weight:400}
.hero-lead{position:absolute;left:305px;top:158px;width:440px;font-family:"Source Sans 3",sans-serif;font-size:24px;line-height:26px;color:var(--hero-grey)}
.hero-visual{position:absolute;left:765px;top:8px;width:235px;height:390px;background:linear-gradient(90deg,#f2f2f4 0%,#eef4fb 15%,#9fc3ea 30%,#d9e8f6 50%,#fafafa 62%,#e8e8ea 100%)}
.slide-pager{position:absolute;left:35px;top:360px;width:85px;height:21px;border-radius:3px;background:var(--purple-light);display:flex;align-items:center;padding-left:3px}
.slide-pager span{width:15px;text-align:center;font-family:"Source Sans 3",sans-serif;font-size:13px;color:#fff}
.slide-pager span.on{background:var(--purple-deep);height:19px;line-height:19px;border-radius:2px}

/* welcome band */
.welcome{position:absolute;left:0;top:436px;width:1040px;height:334px;background:linear-gradient(#4b42a0,var(--purple) 50%,#342b7a)}
.welcome h1{position:absolute;left:45px;top:26px;font-family:"Roboto Condensed",Arial,sans-serif;font-size:24px;color:#fff}
.welcome .intro{position:absolute;left:47px;top:74px;width:560px;font-size:12px;line-height:15.5px;color:var(--on-purple)}
.welcome .intro p+p{margin-top:15.5px}
.offer-list{position:absolute;left:65px;top:178px;list-style:none}
.offer-list li{height:28px;font-size:12.3px;color:var(--on-purple);display:flex;align-items:center;gap:13px}
.offer-list svg{flex:none}
.projects-panel{position:absolute;left:638px;top:21px;width:318px;height:304px;border:1px solid var(--purple-light);border-radius:3px;background:linear-gradient(#5a51ae,#4a42a0 40%,#443b98)}
.projects-panel h2{position:absolute;left:20px;top:10px;font-family:"Roboto Condensed",Arial,sans-serif;font-size:17px;color:#fff}
.projects-panel .rule{position:absolute;left:10px;right:10px;top:40px;height:1px;background:var(--purple-light)}
.project{position:absolute;left:17px;width:290px}
.project .thumb{position:absolute;left:0;top:0;width:66px;height:58px;border:2px solid #e7e7ee;background:linear-gradient(135deg,#8a8fa0,#d8d8de 55%,#5c6070)}
.project p{position:absolute;left:82px;top:0;width:208px;font-size:11px;line-height:15.5px;color:var(--on-purple)}

/* content columns */
.columns{position:absolute;left:0;top:770px;width:1040px;height:355px;background:linear-gradient(#f1f1f4,#fff 60px)}
.col-rule{position:absolute;top:80px;width:1px;height:240px;background:linear-gradient(transparent,#dcdce4,transparent)}
.col-heading{position:absolute;display:flex;align-items:center;gap:9px;font-family:"Source Sans 3",sans-serif;font-size:20px;font-weight:400;color:var(--ink)}
.col-photo{position:absolute;width:260px;height:110px;border:1px solid #c9c9d2;border-radius:8px}
.bullets{position:absolute;list-style:none;width:262px}
.bullets li{position:relative;padding-left:22px;font-size:10.5px;line-height:15.5px;color:var(--body-grey);margin-bottom:12px}
.bullets li svg{position:absolute;left:0;top:2px}
.pill-btn{position:absolute;height:25px;border-radius:13px;background:linear-gradient(#5a50ae,var(--purple-deep));box-shadow:0 0 0 2px #d8d6ea;color:#fff;font-size:12px;display:flex;align-items:center;justify-content:center;gap:12px}
.news-text{position:absolute;left:725px;top:68px;width:245px;font-size:10.5px;line-height:16px;color:var(--body-grey)}
.news-input{position:absolute;left:726px;top:109px;width:204px;height:23px;border:1px solid #c9c9d0;background:#fff}
.feed-label{position:absolute;left:727px;top:187px;font-family:"Roboto Condensed",Arial,sans-serif;font-size:15px;font-weight:400;color:var(--ink)}
.feed-box{position:absolute;left:726px;top:208px;width:254px;height:115px;border:1px solid #cfcfd6;background:#fff;padding:4px}
.feed-inner{background:#f5f5f7;height:100%;padding:8px 2px;font-size:10.2px;line-height:15.5px;color:var(--body-grey)}
.feed-inner a{color:var(--link);text-decoration:none}
.feed-inner small{font-size:8.5px;color:var(--link)}
.feed-follow{position:absolute;right:14px;bottom:14px;display:flex;align-items:center;gap:6px;font-size:11px;font-weight:700;color:var(--link)}
.feed-follow i{display:block;width:22px;height:22px;border-radius:50%;background:#6cc0e8}

/* footer */
.site-footer{position:absolute;left:0;top:1125px;width:1040px;height:75px;background:var(--footer-bg);border-top:2px solid var(--line)}
.site-footer p{position:absolute;left:0;width:1005px;text-align:center;top:30px;font-size:12px;color:#222}
.share{position:absolute;top:26px;width:24px;height:24px;border-radius:3px}
</style>
</head>
<body>

<nav class="main-nav">
  <div class="current-tab"></div>
  <a class="current" style="left:388px">Home</a>
  <a style="left:483px">About Us</a>
  <a style="left:595px">Supply Chain</a>
  <a style="left:686px">Lean</a>
  <a style="left:764px">Interim</a>
  <a style="left:857px">Contact Us</a>
  <a style="left:958px">Projects</a>
</nav>

<header class="hero">
  <div class="brand"><span class="brand-dot"></span><span class="brand-name">Veltrosiga Europe</span></div>
  <p class="hero-lead">Lorem ipsum dolor sit amet, consectetur adipisicing elit, sed do eiusmod tempor incididunt ut labore et dolore magna aliqua...</p>
  <div class="hero-visual" role="img" aria-label="Open white door revealing a blue sky with clouds"></div>
  <div class="slide-pager"><span class="on">1</span><span>2</span><span>3</span><span>4</span><span>5</span></div>
</header>

<section class="welcome">
  <h1>Welcome to Veltrosiga Europe</h1>
  <div class="intro">
    <p>Welcome to Veltrosiga Europe. We have worked with a range of organisations to help them get more out of their operational processes and supply chains. With full end to end supply chain knowledge we can help you identify waste in your supply chains that often get overlooked.</p>
    <p>Before you look to embark on cost reduction plans or a lean journey, get in touch to ensure that your chosen path delivers sustainability and profitable growth.</p>
  </div>
  <ul class="offer-list">
    <li><svg width="10" height="10"><rect width="10" height="10" fill="#e5e5ee"/><path d="M3 2.5L7.5 5 3 7.5z" fill="#2e2670"/></svg>Please click on the above tabs for more details on how we can help with:</li>
    <li><svg width="10" height="10"><rect width="10" height="10" fill="#e5e5ee"/><path d="M3 2.5L7.5 5 3 7.5z" fill="#2e2670"/></svg>Developing an end to end supply chain strategy</li>
    <li><svg width="10" height="10"><rect width="10" height="10" fill="#e5e5ee"/><path d="M3 2.5L7.5 5 3 7.5z" fill="#2e2670"/></svg>Applying Lean to support the strategy</li>
    <li><svg width="10" height="10"><rect width="10" height="10" fill="#e5e5ee"/><path d="M3 2.5L7.5 5 3 7.5z" fill="#2e2670"/></svg>Interim support network to deliver quick wins and rapid cost improvement</li>
    <li><svg width="10" height="10"><rect width="10" height="10" fill="#e5e5ee"/><path d="M3 2.5L7.5 5 3 7.5z" fill="#2e2670"/></svg>Project Management</li>
  </ul>

  <aside class="projects-panel">
    <h2>Business improvement Projects</h2>
    <div class="rule"></div>
    <div class="project" style="top:56px"><div class="thumb" role="img" aria-label="Business people reviewing work at a laptop"></div><p>Lorem ipsum dolor sit amet, consectetur adipisicing elit, sed do eiusmod tempor incididunt ut labore et dolore magna aliqua...</p></div>
    <div class="project" style="top:141px"><div class="thumb" role="img" aria-label="Business people reviewing work at a laptop"></div><p>Lorem ipsum dolor sit amet, consectetur adipisicing elit, sed do eiusmod tempor incididunt ut labore et dolore magna aliqua...</p></div>
    <div class="project" style="top:230px"><div class="thumb" role="img" aria-label="Business people reviewing work at a laptop"></div><p>Lorem ipsum dolor sit amet, consectetur adipisicing elit, sed do eiusmod tempor incididunt ut labore et dolore magna aliqua...</p></div>
  </aside>
</section>

<main class="columns">
  <div class="col-rule" style="left:350px"></div>
  <div class="col-rule" style="left:693px"></div>

  <h2 class="col-heading" style="left:55px;top:28px"><svg width="17" height="17"><circle cx="8.5" cy="8.5" r="8" fill="#3550c8"/><path d="M6.5 5l5 3.5-5 3.5z" fill="#fff"/></svg>Our Services</h2>
  <div class="col-photo" style="left:45px;top:61px;background:linear-gradient(90deg,#c9b8a8,#a9b6c6 40%,#e8eef4 65%,#7a5a52)" role="img" aria-label="Team meeting around a flip chart"></div>
  <ul class="bullets" style="left:52px;top:185px">
    <li><svg width="9" height="9"><rect width="9" height="9" fill="#ddd"/><path d="M3 2l4 2.5-4 2.5z" fill="#444"/></svg>Lorem ipsum dolor sit amet, consectetur adipisicing elit, sed do eiusmod tempor incididunt ut labore et dolore magna aliqua...</li>
    <li><svg width="9" height="9"><rect width="9" height="9" fill="#ddd"/><path d="M3 2l4 2.5-4 2.5z" fill="#444"/></svg>Lorem ipsum dolor sit amet, consectetur adipisicing elit, sed do eiusmod tempor incididunt ut labore et dolore magna aliqua...</li>
  </ul>
  <div class="pill-btn" style="left:232px;top:299px;width:83px">Read More <svg width="5" height="8"><path d="M0 0l5 4-5 4z" fill="#fff"/></svg></div>

  <h2 class="col-heading" style="left:395px;top:27px"><svg width="17" height="17"><circle cx="8.5" cy="8.5" r="8" fill="#3550c8"/><path d="M6.5 5l5 3.5-5 3.5z" fill="#fff"/></svg>Best Solutions</h2>
  <div class="col-photo" style="left:388px;top:61px;background:linear-gradient(90deg,#8f7a6a,#e8e8ec 35%,#f4f4f6 60%,#bfc4cc)" role="img" aria-label="Smiling business team working at laptops"></div>
  <ul class="bullets" style="left:395px;top:185px">
    <li><svg width="9" height="9"><rect width="9" height="9" fill="#ddd"/><path d="M3 2l4 2.5-4 2.5z" fill="#444"/></svg>Lorem ipsum dolor sit amet, consectetur adipisicing elit, sed do eiusmod tempor incididunt ut labore et dolore magna aliqua...</li>
    <li><svg width="9" height="9"><rect width="9" height="9" fill="#ddd"/><path d="M3 2l4 2.5-4 2.5z" fill="#444"/></svg>Lorem ipsum dolor sit amet, consectetur adipisicing elit, sed do eiusmod tempor incididunt ut labore et dolore magna aliqua...</li>
  </ul>
  <div class="pill-btn" style="left:573px;top:299px;width:83px">Read More <svg width="5" height="8"><path d="M0 0l5 4-5 4z" fill="#fff"/></svg></div>

  <h2 class="col-heading" style="left:723px;top:28px"><svg width="17" height="17"><circle cx="8.5" cy="8.5" r="8" fill="#3550c8"/><path d="M6.5 5l5 3.5-5 3.5z" fill="#fff"/></svg>Newsletter</h2>
  <p class="news-text">Lorem ipsum dolor sit amet, consectetur adipisicing elit, sed do eiusmod tempor incididunt ut labore...</p>
  <div class="news-input"></div>
  <div class="pill-btn" style="left:787px;top:148px;width:82px">Submit <svg width="5" height="8"><path d="M0 0l5 4-5 4z" fill="#fff"/></svg></div>
  <h3 class="feed-label">Quipper Feeds</h3>
  <div class="feed-box">
    <div class="feed-inner">CSS3 vs. CSS: A Speed Benchmark <a>http://qp.io /K5UqCpN</a> I believe in the power, speed and "update-ability" of CSS3. <small>3 days ago</small></div>
    <div class="feed-follow"><i></i>Follow us on quipper</div>
  </div>
</main>

<footer class="site-footer">
  <p>Copyright @ Veltrosiga Europe.com. All Rights Reserved.</p>
  <span class="share" style="left:888px;background:#3b5a9a" aria-label="chatterbox"></span>
  <span class="share" style="left:919px;background:#3aa8e0" aria-label="quipper"></span>
  <span class="share" style="left:954px;background:#e8731e" aria-label="feed"></span>
</footer>

</body>
</html>
```